Natural & Organic Skin Care Line labels

TALUBRA is start up company for all natural and organic beauty products needing labels. KISS method/less is more so no graphics. would like "natural background color" black faunts, pop of color matching scent. Will attach example I made on Mac Word.
Updates

I would like to thank the designers for very nice work.  Believing I jumped the gun with a project I was not fully prepared for, I am placing it on hold.

Target Market(s)

Mostly women with middle to upper income

Industry/Entity Type

It Company

Requirements
Must have
• Cosmetic labeling requires labels list INCI (attached example), and Net Wt.

```html
<!DOCTYPE html>
<html lang="en">
<head>
<meta charset="utf-8">
<title>TALUBRA Organic — Whipped Lip Butter Labels</title>
<link rel="stylesheet" href="https://fonts.googleapis.com/css2?family=Didact+Gothic&family=Delius&family=Cedarville+Cursive&family=Arimo:wght@400;700&family=Tinos&display=swap">
<style>
  :root {
    --backdrop: #6d6d6d;
    --backdrop-light: #8a8a8a;
    --label-fill: #e4d2ad;
    --label-fill-light: #ead9b6;
    --label-rim: #c29a6a;
    --ink: #2a2520;
    --band-orange: #e8791b;
    --band-cream: #f8f0c8;
    --band-lemon: #fdf87c;
    --band-orange-vanilla: #e0a46b;
    --band-peppermint: #c6d94b;
  }
  * { margin: 0; padding: 0; box-sizing: border-box; }
  html, body { width: 1200px; height: 834px; overflow: hidden; }
  body {
    position: relative;
    background: radial-gradient(ellipse at 50% 40%, var(--backdrop-light) 0%, var(--backdrop) 65%);
    color: var(--ink);
  }
  .label {
    position: absolute;
    width: 334px;
    height: 334px;
    border-radius: 50%;
    border: 8px solid var(--label-rim);
    background: radial-gradient(circle at 40% 35%, var(--label-fill-light), var(--label-fill) 70%);
    overflow: hidden;
    text-align: center;
  }
  .label__brand, .label__line {
    position: absolute;
    left: 0; right: 0;
    font-family: "Didact Gothic", "Century Gothic", sans-serif;
    font-size: 31px;
    line-height: 1;
  }
  .label__brand { top: 22px; }
  .label__line { top: 58px; }
  .label__band {
    position: absolute;
    left: 0; right: 0;
    top: 104px;
    height: 58px;
    display: flex;
    align-items: center;
    justify-content: center;
    font-family: "Delius", sans-serif;
    font-size: 27px;
  }
  .label__scent {
    position: absolute;
    left: 0; right: 0;
    top: 170px;
    font-family: "Cedarville Cursive", cursive;
    font-size: 25px;
    line-height: 1.2;
    font-weight: bold;
  }
  .label__scent--large { font-size: 30px; top: 165px; }
  .label__inci {
    position: absolute;
    left: 46px; right: 46px;
    top: 206px;
    font-family: "Arimo", Arial, sans-serif;
    font-size: 9px;
    line-height: 1.28;
  }
  .label__inci strong { font-weight: 700; }
  .label__weight {
    position: absolute;
    left: 0; right: 0;
    top: 280px;
    font-family: "Tinos", "Times New Roman", serif;
    font-size: 13px;
  }
  .label--orange-lemongrass { left: 51px;  top: 95px; }
  .label--vanilla-sandalwood { left: 428px; top: 95px; }
  .label--lemon { left: 802px; top: 95px; }
  .label--orange-vanilla { left: 226px; top: 430px; }
  .label--peppermint { left: 618px; top: 430px; }
  .label--orange-lemongrass .label__band { background: var(--band-orange); }
  .label--vanilla-sandalwood .label__band { background: var(--band-cream); }
  .label--lemon .label__band { background: var(--band-lemon); }
  .label--orange-vanilla .label__band { background: var(--band-orange-vanilla); }
  .label--peppermint .label__band { background: var(--band-peppermint); }
</style>
</head>
<body>

<section class="label label--orange-lemongrass">
  <div class="label__brand">TALUBRA</div>
  <div class="label__line">Organic</div>
  <div class="label__band">Whipped Lip Butter</div>
  <div class="label__scent">Orange Lemongrass</div>
  <p class="label__inci"><strong>INCI:</strong> CymbopogonSchoenathus (Lemongrass) Oil, Citrus AurantiumDulcis (Organic Orange) Peel Oil, ButyrospermumParkii (Organic Shea) Butter, Beeswax, CocosNucifera (Organic Coconut) Oil, Rosa Mosqueta (Organic Rose Hip) Oil, RosmarinusOfficinalis (Rosemary) Leaf Extract, Tocopherol (Vitamin E)</p>
  <div class="label__weight">Net Wt. .30oz(8.5g)</div>
</section>

<section class="label label--vanilla-sandalwood">
  <div class="label__brand">TALUBRA</div>
  <div class="label__line">Organic</div>
  <div class="label__band">Whipped Lip Butter</div>
  <div class="label__scent">Vanilla &amp; Sandlewood</div>
  <p class="label__inci"><strong>INCI:</strong>Santalum Album (Organic Sandlewood) Oil, Vanilla PlanifoliaExract, Flavor (Aroma), ButyrospermumParkii (Organic Shea) Butter, Beeswax, CocosNucifera (Organic Coconut) Oil, Rosa Mosqueta (Organic Rose Hip) Oil, RosmarinusOfficinalis (Rosemary) Leaf Extract, Tocopherol (Vitamin E)</p>
  <div class="label__weight">Net Wt. .30oz(8.5g)</div>
</section>

<section class="label label--lemon">
  <div class="label__brand">TALUBRA</div>
  <div class="label__line">Organic</div>
  <div class="label__band">Whipped Lip Butter</div>
  <div class="label__scent label__scent--large">Lemon</div>
  <p class="label__inci"><strong>INCI:</strong> Citrus Limonium (Lemon) Oil, ButyrospermumParkii (Organic Shea) Butter, Beeswax, CocosNucifera (Organic Coconut) Oil, Rosa Mosqueta (Organic Rose Hip) Oil, RosmarinusOfficinalis (Rosemary) Leaf Extract, Tocopherol (Vitamin E)</p>
  <div class="label__weight">Net Wt. .30oz(8.5g)</div>
</section>

<section class="label label--orange-vanilla">
  <div class="label__brand">TALUBRA</div>
  <div class="label__line">Organic</div>
  <div class="label__band">Whipped Lip Butter</div>
  <div class="label__scent">Orange Vanilla</div>
  <p class="label__inci"><strong>INCI:</strong> Citrus Sinensis (Orange) Oil, Flavor (Aroma) Vanilla Planifolia Extract, ButyrospermumParkii (Organic Shea) Butter, Beeswax, CocosNucifera (Organic Coconut) Oil, Rosa Mosqueta (Organic Rose Hip) Oil, RosmarinusOfficinalis (Rosemary) Leaf Extract, Tocopherol (Vitamin E)</p>
  <div class="label__weight">Net Wt. .30oz(8.5g)</div>
</section>

<section class="label label--peppermint">
  <div class="label__brand">TALUBRA</div>
  <div class="label__line">Organic</div>
  <div class="label__band">Whipped Lip Butter</div>
  <div class="label__scent">Peppermint</div>
  <p class="label__inci"><strong>INCI:</strong> MenthaPiperita (Peppermint) Oil, ButyrospermumParkii (Organic Shea) Butter, Beeswax, CocosNucifera (Organic Coconut) Oil, Rosa Mosqueta (Organic Rose Hip) Oil, RosmarinusOfficinalis (Rosemary) Leaf Extract, Tocopherol (Vitamin E)</p>
  <div class="label__weight">Net Wt. .30oz(8.5g)</div>
</section>

</body>
</html>
```